Consulting company business cards

We have a base design, but would be willing to update. We have a new logo/"tag" that needs to be added. Current business card design is attached for reference into our "style."

Industry/Entity Type

Business

Contact Information for Business Card

Should contain name and title, office number, mobile number if appropriate, e-mail, website, physical address, and company logo.

Font styles to use
Other font styles liked:
• See current card design on GorvandBCard

Colors
0455a3
85acd3
aaaaaa

Requirements
Must have
• Our colors are navy blue, gray, and a lighter blue
Nice to have
• Design that I can easily drop in new names/titles as we hire employees.

```html
<!DOCTYPE html>
<html lang="en">
<head>
<meta charset="utf-8">
<title>Harlow — Business Cards</title>
<link href="https://fonts.googleapis.com/css2?family=Anton&family=Jost:wght@400;500&family=Raleway:wght@500&display=swap" rel="stylesheet">
<style>
  :root {
    --backdrop: #2b2d31;
    --navy: #0a3352;
    --navy-deep: #072a44;
    --emblem-blue: #85acd3;
    --band-sky: #35a7dc;
    --band-royal: #2f6fb1;
    --band-mist: #85acd3;
    --band-ice: #8ccbe5;
    --band-ocean: #1b8fcf;
    --text-soft: #9fc4e2;
    --white: #ffffff;
  }
  * { box-sizing: border-box; margin: 0; padding: 0; }
  html, body { width: 1200px; height: 900px; overflow: hidden; }
  body { background: var(--backdrop); position: relative; font-family: "Jost", sans-serif; }

  .card {
    position: absolute;
    width: 560px;
    height: 320px;
    background: var(--navy);
    border-radius: 4px;
    overflow: hidden;
    box-shadow: 0 14px 30px rgba(0,0,0,.45);
  }
  .card--contact { left: 70px; top: 110px; }
  .card--brand { left: 570px; top: 470px; background: linear-gradient(160deg, var(--navy) 0%, var(--navy-deep) 100%); }

  /* contact side */
  .emblem-area {
    position: absolute;
    left: 38px; top: 78px;
    width: 220px; height: 210px;
    background: var(--emblem-blue);
    border-radius: 46% 54% 48% 52% / 44% 40% 60% 56%;
  }
  .identity {
    position: absolute;
    left: 250px; top: 22px;
    color: var(--text-soft);
    line-height: 1.15;
  }
  .identity__title { font-size: 17px; font-weight: 400; }
  .identity__name { font-size: 20px; font-weight: 500; padding-left: 14px; }

  .details { list-style: none; }
  .detail {
    position: absolute;
    right: -20px;
    height: 38px;
    border-radius: 19px 0 0 19px;
    display: flex;
    align-items: center;
    color: var(--white);
    font-size: 15px;
    line-height: 1.05;
  }
  .detail__icon {
    width: 30px; height: 30px;
    margin: 0 10px 0 4px;
    border-radius: 50%;
    background: rgba(255,255,255,.18);
    display: flex; align-items: center; justify-content: center;
    flex-shrink: 0;
  }
  .detail__icon svg { width: 18px; height: 18px; }
  .detail--mobile  { top: 84px;  left: 282px; background: var(--band-sky); }
  .detail--office  { top: 126px; left: 304px; background: var(--band-royal); }
  .detail--email   { top: 168px; left: 326px; background: var(--band-mist); }
  .detail--web     { top: 210px; left: 348px; background: var(--band-ice); }
  .detail--address { top: 252px; left: 370px; background: var(--band-ocean); font-size: 14px; }

  /* brand side */
  .brand {
    position: absolute;
    left: 0; right: 0; top: 92px;
    text-align: center;
    color: var(--white);
  }
  .brand__lockup { display: inline-flex; align-items: center; gap: 18px; }
  .brand__name {
    font-family: "Anton", sans-serif;
    font-size: 92px;
    letter-spacing: 4px;
    line-height: 1;
  }
  .brand__mark {
    width: 52px; height: 52px;
    border-radius: 50%;
    background: var(--white);
  }
  .brand__tagline {
    margin-top: 12px;
    font-family: "Raleway", sans-serif;
    font-weight: 500;
    font-size: 17px;
    letter-spacing: 5px;
  }
</style>
</head>
<body>

<section class="card card--contact" aria-label="Business card, contact side">
  <div class="emblem-area" role="img" aria-label="Brand emblem illustration area"></div>

  <div class="identity">
    <p class="identity__title">Title</p>
    <p class="identity__name">Name and Surname</p>
  </div>

  <ul class="details">
    <li class="detail detail--mobile">
      <span class="detail__icon"><svg viewBox="0 0 24 24" fill="none" stroke="#fff" stroke-width="2"><rect x="7" y="2" width="10" height="20" rx="2"/><line x1="11" y1="18" x2="13" y2="18"/></svg></span>
      mobile number
    </li>
    <li class="detail detail--office">
      <span class="detail__icon"><svg viewBox="0 0 24 24" fill="#fff"><path d="M6.6 10.8a15 15 0 0 0 6.6 6.6l2.2-2.2a1 1 0 0 1 1-.25 11.4 11.4 0 0 0 3.6.57 1 1 0 0 1 1 1V20a1 1 0 0 1-1 1A17 17 0 0 1 3 4a1 1 0 0 1 1-1h3.5a1 1 0 0 1 1 1c0 1.25.2 2.45.57 3.6a1 1 0 0 1-.25 1z"/></svg></span>
      office number
    </li>
    <li class="detail detail--email">
      <span class="detail__icon"><svg viewBox="0 0 24 24" fill="none" stroke="#fff" stroke-width="2"><rect x="3" y="5" width="18" height="14" rx="1"/><polyline points="3,6 12,13 21,6"/></svg></span>
      e-mail
    </li>
    <li class="detail detail--web">
      <span class="detail__icon"><svg viewBox="0 0 24 24" fill="none" stroke="#fff" stroke-width="1.6"><circle cx="12" cy="12" r="9"/><ellipse cx="12" cy="12" rx="4" ry="9"/><line x1="3" y1="12" x2="21" y2="12"/><line x1="5" y1="7" x2="19" y2="7"/><line x1="5" y1="17" x2="19" y2="17"/></svg></span>
      web site
    </li>
    <li class="detail detail--address">
      <span class="detail__icon"><svg viewBox="0 0 24 24" fill="none" stroke="#fff" stroke-width="2"><path d="M12 22s7-7.5 7-12.5a7 7 0 0 0-14 0C5 14.5 12 22 12 22z"/><circle cx="12" cy="9.5" r="2.5"/></svg></span>
      <span>physical<br>address</span>
    </li>
  </ul>
</section>

<section class="card card--brand" aria-label="Business card, brand side">
  <div class="brand">
    <div class="brand__lockup">
      <span class="brand__name">HARLOW</span>
      <span class="brand__mark" aria-hidden="true"></span>
    </div>
    <p class="brand__tagline">A CLOUD CONSULTING COMPANY</p>
  </div>
</section>

</body>
</html>
```